2026 Calendar Design for Construction Company

2026 Calendar for a underground utility construction company January - December 2026 all on one long page lnwarbeck.com is our website Safety Quality Production is our slogan

```html
<!DOCTYPE html>
<html lang="en">
<head>
<meta charset="utf-8">
<title>LN Warbeck 2026 Calendar</title>
<link rel="stylesheet" href="https://fonts.googleapis.com/css2?family=Archivo:wght@700;800;900&display=swap">
<style>
  :root {
    --paper: #efeeea;
    --ink: #111111;
    --band: #141414;
    --yellow: #f2d21b;
    --sat: #f4e48a;
    --white: #ffffff;
    --photo-sky: #9db8d2;
    --photo-ground: #6e5a43;
  }
  * { margin: 0; padding: 0; box-sizing: border-box; }
  html, body { width: 670px; height: 1200px; overflow: hidden; }
  body {
    background: var(--paper);
    font-family: "Archivo", Arial, sans-serif;
    color: var(--ink);
    position: relative;
  }
  .brand {
    position: absolute; top: 78px; left: 0; width: 670px;
    display: flex; justify-content: center; align-items: center; gap: 12px;
  }
  .brand-mark { width: 22px; height: 22px; background: var(--yellow); }
  .brand-name { font-size: 44px; font-weight: 900; color: var(--ink); letter-spacing: 0.5px; }

  .slogan-band {
    position: absolute; top: 199px; left: 0; width: 670px; height: 73px;
    background: var(--band);
    border-top: 5px solid var(--yellow); border-bottom: 5px solid var(--yellow);
    display: flex; align-items: center; justify-content: center;
  }
  .slogan-band svg { position: absolute; top: -5px; height: 73px; }
  .slogan-band .edge-left { left: 14px; }
  .slogan-band .edge-right { right: 14px; }
  .slogan {
    color: var(--white); font-size: 28px; font-weight: 900; letter-spacing: 0.3px;
    white-space: nowrap;
  }
  .slogan .dot { color: var(--yellow); }

  .calendar {
    position: absolute; top: 299px; left: 37px; width: 596px;
    display: grid; grid-template-columns: repeat(4, 138px); grid-auto-rows: 134px;
    column-gap: 15.3px; row-gap: 18px;
  }
  .month-name {
    background: var(--band); color: var(--white);
    font-size: 17px; font-weight: 800; text-align: center;
    height: 25px; line-height: 25px;
  }
  .days {
    display: grid; grid-template-columns: repeat(7, 1fr);
    font-size: 11.5px; font-weight: 700; text-align: center;
    margin-top: 2px;
  }
  .days > * { height: 15.4px; line-height: 15.4px; font-style: normal; }
  .days > .head { font-size: 10px; }
  .days > :nth-child(7n) { background: var(--sat); }

  .site-photo {
    position: absolute; top: 755px; left: 37px; width: 596px; height: 306px;
    border: 1.5px solid var(--ink);
    background: linear-gradient(180deg, var(--photo-sky) 0%, #dfe6ea 45%, #8f9a62 52%, var(--photo-ground) 100%);
  }

  .footer-rule { position: absolute; top: 1083px; left: 0; width: 670px; height: 5px; background: var(--yellow); }
  .footer {
    position: absolute; top: 1090px; left: 0; width: 670px; height: 70px;
    background: var(--band);
  }
  .badge {
    position: absolute; left: 63px; top: 12px; width: 46px; height: 46px;
    border-radius: 50%; background: #3e7a35;
  }
  .website {
    position: absolute; left: 0; width: 670px; top: 0; height: 70px; line-height: 70px;
    text-align: center; color: var(--white); font-size: 36px; font-weight: 800;
  }
</style>
</head>
<body>
  <header class="brand">
    <span class="brand-mark"></span>
    <span class="brand-name">LN Warbeck</span>
  </header>

  <div class="slogan-band">
    <svg class="edge-left" width="20" viewBox="0 0 20 73"><polygon points="12,0 20,0 8,73 0,73" fill="#f2d21b"/></svg>
    <p class="slogan">SAFETY <span class="dot">•</span> QUALITY <span class="dot">•</span> PRODUCTION</p>
    <svg class="edge-right" width="20" viewBox="0 0 20 73"><polygon points="12,0 20,0 8,73 0,73" fill="#f2d21b"/></svg>
  </div>

  <main class="calendar">
    <section class="month"><h2 class="month-name">JANUARY</h2><div class="days"><b class="head">S</b><b class="head">M</b><b class="head">T</b><b class="head">W</b><b class="head">T</b><b class="head">F</b><b class="head">S</b><i></i><i></i><i></i><i></i><i>1</i><i>2</i><i>3</i><i>4</i><i>5</i><i>6</i><i>7</i><i>8</i><i>9</i><i>10</i><i>11</i><i>12</i><i>13</i><i>14</i><i>15</i><i>16</i><i>17</i><i>18</i><i>19</i><i>20</i><i>21</i><i>22</i><i>23</i><i>24</i><i>25</i><i>26</i><i>27</i><i>28</i><i>29</i><i>30</i><i>31</i></div></section>
    <section class="month"><h2 class="month-name">FEBRUARY</h2><div class="days"><b class="head">S</b><b class="head">M</b><b class="head">T</b><b class="head">W</b><b class="head">T</b><b class="head">F</b><b class="head">S</b><i>1</i><i>2</i><i>3</i><i>4</i><i>5</i><i>6</i><i>7</i><i>8</i><i>9</i><i>10</i><i>11</i><i>12</i><i>13</i><i>14</i><i>15</i><i>16</i><i>17</i><i>18</i><i>19</i><i>20</i><i>21</i><i>22</i><i>23</i><i>24</i><i>25</i><i>26</i><i>27</i><i>28</i></div></section>
    <section class="month"><h2 class="month-name">MARCH</h2><div class="days"><b class="head">S</b><b class="head">M</b><b class="head">T</b><b class="head">W</b><b class="head">T</b><b class="head">F</b><b class="head">S</b><i>1</i><i>2</i><i>3</i><i>4</i><i>5</i><i>6</i><i>7</i><i>8</i><i>9</i><i>10</i><i>11</i><i>12</i><i>13</i><i>14</i><i>15</i><i>16</i><i>17</i><i>18</i><i>19</i><i>20</i><i>21</i><i>22</i><i>23</i><i>24</i><i>25</i><i>26</i><i>27</i><i>28</i><i>29</i><i>30</i><i>31</i></div></section>
    <section class="month"><h2 class="month-name">APRIL</h2><div class="days"><b class="head">S</b><b class="head">M</b><b class="head">T</b><b class="head">W</b><b class="head">T</b><b class="head">F</b><b class="head">S</b><i></i><i></i><i></i><i>1</i><i>2</i><i>3</i><i>4</i><i>5</i><i>6</i><i>7</i><i>8</i><i>9</i><i>10</i><i>11</i><i>12</i><i>13</i><i>14</i><i>15</i><i>16</i><i>17</i><i>18</i><i>19</i><i>20</i><i>21</i><i>22</i><i>23</i><i>24</i><i>25</i><i>26</i><i>27</i><i>28</i><i>29</i><i>30</i></div></section>
    <section class="month"><h2 class="month-name">MAY</h2><div class="days"><b class="head">S</b><b class="head">M</b><b class="head">T</b><b class="head">W</b><b class="head">T</b><b class="head">F</b><b class="head">S</b><i></i><i></i><i></i><i></i><i></i><i>1</i><i>2</i><i>3</i><i>4</i><i>5</i><i>6</i><i>7</i><i>8</i><i>9</i><i>10</i><i>11</i><i>12</i><i>13</i><i>14</i><i>15</i><i>16</i><i>17</i><i>18</i><i>19</i><i>20</i><i>21</i><i>22</i><i>23</i><i>24</i><i>25</i><i>26</i><i>27</i><i>28</i><i>29</i><i>30</i><i>31</i></div></section>
    <section class="month"><h2 class="month-name">JUNE</h2><div class="days"><b class="head">S</b><b class="head">M</b><b class="head">T</b><b class="head">W</b><b class="head">T</b><b class="head">F</b><b class="head">S</b><i></i><i>1</i><i>2</i><i>3</i><i>4</i><i>5</i><i>6</i><i>7</i><i>8</i><i>9</i><i>10</i><i>11</i><i>12</i><i>13</i><i>14</i><i>15</i><i>16</i><i>17</i><i>18</i><i>19</i><i>20</i><i>21</i><i>22</i><i>23</i><i>24</i><i>25</i><i>26</i><i>27</i><i>28</i><i>29</i><i>30</i></div></section>
    <section class="month"><h2 class="month-name">JULY</h2><div class="days"><b class="head">S</b><b class="head">M</b><b class="head">T</b><b class="head">W</b><b class="head">T</b><b class="head">F</b><b class="head">S</b><i></i><i></i><i></i><i>1</i><i>2</i><i>3</i><i>4</i><i>5</i><i>6</i><i>7</i><i>8</i><i>9</i><i>10</i><i>11</i><i>12</i><i>13</i><i>14</i><i>15</i><i>16</i><i>17</i><i>18</i><i>19</i><i>20</i><i>21</i><i>22</i><i>23</i><i>24</i><i>25</i><i>26</i><i>27</i><i>28</i><i>29</i><i>30</i><i>31</i></div></section>
    <section class="month"><h2 class="month-name">AUGUST</h2><div class="days"><b class="head">S</b><b class="head">M</b><b class="head">T</b><b class="head">W</b><b class="head">T</b><b class="head">F</b><b class="head">S</b><i></i><i></i><i></i><i></i><i></i><i></i><i>1</i><i>2</i><i>3</i><i>4</i><i>5</i><i>6</i><i>7</i><i>8</i><i>9</i><i>10</i><i>11</i><i>12</i><i>13</i><i>14</i><i>15</i><i>16</i><i>17</i><i>18</i><i>19</i><i>20</i><i>21</i><i>22</i><i>23</i><i>24</i><i>25</i><i>26</i><i>27</i><i>28</i><i>29</i><i>30</i><i>31</i></div></section>
    <section class="month"><h2 class="month-name">SEPTEMBER</h2><div class="days"><b class="head">S</b><b class="head">M</b><b class="head">T</b><b class="head">W</b><b class="head">T</b><b class="head">F</b><b class="head">S</b><i></i><i></i><i>1</i><i>2</i><i>3</i><i>4</i><i>5</i><i>6</i><i>7</i><i>8</i><i>9</i><i>10</i><i>11</i><i>12</i><i>13</i><i>14</i><i>15</i><i>16</i><i>17</i><i>18</i><i>19</i><i>20</i><i>21</i><i>22</i><i>23</i><i>24</i><i>25</i><i>26</i><i>27</i><i>28</i><i>29</i><i>30</i></div></section>
    <section class="month"><h2 class="month-name">OCTOBER</h2><div class="days"><b class="head">S</b><b class="head">M</b><b class="head">T</b><b class="head">W</b><b class="head">T</b><b class="head">F</b><b class="head">S</b><i></i><i></i><i></i><i></i><i>1</i><i>2</i><i>3</i><i>4</i><i>5</i><i>6</i><i>7</i><i>8</i><i>9</i><i>10</i><i>11</i><i>12</i><i>13</i><i>14</i><i>15</i><i>16</i><i>17</i><i>18</i><i>19</i><i>20</i><i>21</i><i>22</i><i>23</i><i>24</i><i>25</i><i>26</i><i>27</i><i>28</i><i>29</i><i>30</i><i>31</i></div></section>
    <section class="month"><h2 class="month-name">NOVEMBER</h2><div class="days"><b class="head">S</b><b class="head">M</b><b class="head">T</b><b class="head">W</b><b class="head">T</b><b class="head">F</b><b class="head">S</b><i>1</i><i>2</i><i>3</i><i>4</i><i>5</i><i>6</i><i>7</i><i>8</i><i>9</i><i>10</i><i>11</i><i>12</i><i>13</i><i>14</i><i>15</i><i>16</i><i>17</i><i>18</i><i>19</i><i>20</i><i>21</i><i>22</i><i>23</i><i>24</i><i>25</i><i>26</i><i>27</i><i>28</i><i>29</i><i>30</i></div></section>
    <section class="month"><h2 class="month-name">DECEMBER</h2><div class="days"><b class="head">S</b><b class="head">M</b><b class="head">T</b><b class="head">W</b><b class="head">T</b><b class="head">F</b><b class="head">S</b><i></i><i></i><i>1</i><i>2</i><i>3</i><i>4</i><i>5</i><i>6</i><i>7</i><i>8</i><i>9</i><i>10</i><i>11</i><i>12</i><i>13</i><i>14</i><i>15</i><i>16</i><i>17</i><i>18</i><i>19</i><i>20</i><i>21</i><i>22</i><i>23</i><i>24</i><i>25</i><i>26</i><i>27</i><i>28</i><i>29</i><i>30</i><i>31</i></div></section>
  </main>

  <div class="site-photo" role="img" aria-label="Photo of an underground utility job site: an excavator digging a trench beside a horizontal directional drill, with crew members in hi-vis vests under a cloudy sky"></div>

  <div class="footer-rule"></div>
  <footer class="footer">
    <span class="badge" aria-hidden="true"></span>
    <p class="website">lnwarbeck.com</p>
  </footer>
</body>
</html>
```